UPDATED BRIEF: We are looking for a trade show booth design - The design is for 10ft x 10 ft booth curved booth display.
we want to utilize the laptop image more with a half wheel of the key services on our platform.
Strategic DEI Business Partner Workshops
Leader to Leader Training
ERG Leader Strategic Training
15 - Microlearning Labs
Coaching & Mentorship
DEI Research, Articles and Hot topics

With the tagline: Experience the Power of Strategic DEI Training and Peer-to-Peer Support on One Platform

About us: we are a learning and development community for diversity and inclusion and talent management professionals. Our corporate colors are blue, 004AAD
We are looking for a clean, corporate design that makes someone feel included. The moment you look at it, you feel included. We may add a screenshot of the Brightpath Growth Hub platform. Our logo will be included and our tagline is

"Together We Can Create a More Inclusive Future: The Brightpath Growth Hub Community for DEI and Talent Leaders."

We have two versions of our logo - one with text only the other with the logo design. We're not sure which one we want to use.

Target Market(s)

Human Resources and Talent Leaders

Industry/Entity Type

Training and development

Colors
0054AA
0677BA
7BADD7
CADEEF
E8F1F8
F0912C
F2A743
F7CA91
FBE8D2
FDF5EE
EB3D1F
EC4F4E
F09395
F8D3D4
FCEDEE

Requirements
Must have
• Must have logo and good visual design
Should not have
• I've added the examples of what I am looking for

```html
<!DOCTYPE html>
<html lang="en">
<head>
<meta charset="utf-8">
<title>Brightpath Growth Hub – Booth Backdrop</title>
<link href="https://fonts.googleapis.com/css2?family=Montserrat:wght@500;600;700;800&display=swap" rel="stylesheet">
<style>
  :root {
    --page-bg: #9a9a9a;
    --brand-blue: #0d47b8;
    --brand-blue-deep: #0a3a9e;
    --band-navy: #0e1630;
    --white: #ffffff;
    --line: rgba(255,255,255,0.95);
    --screen-dark: #1b2340;
    --screen-light: #eef1f6;
  }
  * { margin: 0; padding: 0; box-sizing: border-box; }
  html, body { width: 833px; height: 1200px; overflow: hidden; }
  body {
    background: var(--page-bg);
    font-family: "Montserrat", Arial, sans-serif;
    color: var(--white);
    position: relative;
  }
  .backdrop {
    position: absolute;
    left: 20px; top: 352px;
    width: 793px; height: 496px;
    background: linear-gradient(180deg, var(--brand-blue) 0%, var(--brand-blue-deep) 100%);
    box-shadow: 0 6px 18px rgba(0,0,0,0.35);
    overflow: hidden;
  }
  .side-band {
    position: absolute; top: 0; width: 74px; height: 100%;
    background: var(--band-navy);
    display: flex; align-items: center; justify-content: center;
  }
  .side-band--left { left: 0; border-right: 1px dashed rgba(255,255,255,0.6); }
  .side-band--right { right: 0; border-left: 1px dashed rgba(255,255,255,0.6); }
  .side-band__url {
    font-size: 14px; letter-spacing: 1.2px; white-space: nowrap; font-weight: 500;
  }
  .side-band--left .side-band__url { transform: rotate(-90deg); }
  .side-band--right .side-band__url { transform: rotate(90deg); }
  .side-band__url strong, .url-bar strong { font-weight: 700; }

  .brand-name {
    position: absolute; left: 74px; right: 74px; top: 34px;
    text-align: center; font-size: 30px; font-weight: 800; letter-spacing: 0.5px;
    line-height: 1.1;
  }
  .headline {
    position: absolute; left: 74px; right: 74px; top: 116px;
    text-align: center; font-size: 21px; font-weight: 800; letter-spacing: 0.8px;
    line-height: 25px; text-transform: uppercase;
  }
  .tagline {
    position: absolute; left: 74px; right: 74px; top: 176px;
    text-align: center; font-size: 12px; font-weight: 600; letter-spacing: 0.6px;
    line-height: 15px;
  }
  .service-wheel { position: absolute; left: 0; top: 0; }
  .service {
    position: absolute; width: 148px; height: 30px;
    border: 1.2px solid var(--line); border-radius: 4px;
    display: flex; align-items: center; justify-content: center; text-align: center;
    font-size: 7.6px; font-weight: 700; letter-spacing: 0.8px; line-height: 9.5px;
    text-transform: uppercase;
  }
  .service--left { left: 96px; }
  .service--right { left: 549px; }
  .platform-screenshot {
    position: absolute; left: 306px; top: 257px; width: 182px; height: 124px;
    border-radius: 6px;
    background: linear-gradient(90deg, var(--screen-dark) 0%, var(--screen-dark) 30%, var(--screen-light) 30%, var(--screen-light) 100%);
    border: 4px solid #222;
    border-bottom-width: 8px;
  }
  .url-bar {
    position: absolute; left: 244px; top: 439px; width: 305px; height: 30px;
    background: var(--band-navy);
    display: flex; align-items: center; justify-content: center;
    font-size: 11.5px; letter-spacing: 1.3px; font-weight: 500;
  }
</style>
</head>
<body>
  <main class="backdrop">
    <aside class="side-band side-band--left"><span class="side-band__url">WWW.<strong>BRIGHTPATHGROWTHHUB</strong>.COM</span></aside>
    <aside class="side-band side-band--right"><span class="side-band__url">WWW.<strong>BRIGHTPATHGROWTHHUB</strong>.COM</span></aside>

    <div class="brand-name">Brightpath Growth Hub</div>
    <h1 class="headline">The Brightpath Growth Hub Community<br>for DEI and Talent Leaders</h1>
    <p class="tagline">Experience The Power Of Strategic DEI Training &amp; Peer-to-Peer<br>Support On One Platform</p>

    <svg class="service-wheel" width="793" height="496" viewBox="0 0 793 496" aria-hidden="true">
      <g fill="none" stroke="#ffffff" stroke-width="1.3">
        <path d="M244 241 A94.7 94.7 0 0 1 244 401"/>
        <path d="M549 241 A94.7 94.7 0 0 0 549 401"/>
        <line x1="244" y1="281" x2="279" y2="280"/>
        <line x1="244" y1="321" x2="288" y2="321"/>
        <line x1="244" y1="361" x2="279" y2="361"/>
        <line x1="514" y1="280" x2="549" y2="281"/>
        <line x1="505" y1="321" x2="549" y2="321"/>
        <line x1="514" y1="361" x2="549" y2="361"/>
      </g>
      <g fill="#0d47b8" stroke="#ffffff" stroke-width="1.5">
        <circle cx="244" cy="241" r="3.5"/><circle cx="279" cy="280" r="3.5"/>
        <circle cx="288" cy="321" r="3.5"/><circle cx="279" cy="361" r="3.5"/>
        <circle cx="244" cy="401" r="3.5"/>
        <circle cx="549" cy="241" r="3.5"/><circle cx="514" cy="280" r="3.5"/>
        <circle cx="505" cy="321" r="3.5"/><circle cx="514" cy="361" r="3.5"/>
        <circle cx="549" cy="401" r="3.5"/>
      </g>
    </svg>

    <div class="service service--left" style="top:266px">Strategic DEI Business<br>Partner Workshops</div>
    <div class="service service--left" style="top:306px">Leader to Leader<br>Training</div>
    <div class="service service--left" style="top:346px">ERG Leader Strategic<br>Training</div>
    <div class="service service--right" style="top:266px">15 - Microlearning<br>Labs</div>
    <div class="service service--right" style="top:306px">Coaching and<br>Mentorship</div>
    <div class="service service--right" style="top:346px">DEI Research, Articles<br>and Hot Topics</div>

    <div class="platform-screenshot" role="img" aria-label="Laptop showing the community platform home screen"></div>

    <div class="url-bar">WWW.<strong>BRIGHTPATHGROWTHHUB</strong>.COM</div>
  </main>
</body>
</html>
```